LedgaVue Business Card

We need a business card design using the attached logo. The company is a financial services company that provides a dashboard (chart based information) for Executives of small businesses to use to better manage their information. The design must be progressive, make good utilization of the logo and project stability and financial security.

Industry/Entity Type

Financial

```html
<!DOCTYPE html>
<html lang="en">
<head>
<meta charset="utf-8">
<title>LedgaVue Business Card</title>
<link href="https://fonts.googleapis.com/css2?family=Mulish:wght@400;700;800&display=swap" rel="stylesheet">
<style>
  :root {
    --brand-red: #9b1b1e;
    --ink: #111111;
    --paper: #ffffff;
  }
  html, body {
    margin: 0;
    padding: 0;
    width: 1050px;
    height: 1200px;
    overflow: hidden;
    background: var(--paper);
  }
  .card {
    position: relative;
    width: 1050px;
    height: 1200px;
    background: var(--paper);
    font-family: "Mulish", "Helvetica Neue", Arial, sans-serif;
    color: var(--ink);
  }
  .hero-band {
    position: absolute;
    left: 0;
    top: 0;
    width: 1050px;
    height: 600px;
    background: var(--brand-red);
    display: flex;
    align-items: center;
    justify-content: center;
  }
  .hero-name {
    color: var(--paper);
    font-weight: 800;
    font-size: 110px;
    letter-spacing: -1px;
    line-height: 1;
  }
  .details {
    position: absolute;
    left: 45px;
    top: 650px;
  }
  .employee-name {
    margin: 0;
    font-weight: 700;
    font-size: 30px;
    line-height: 38px;
  }
  .job-title {
    margin: 2px 0 0;
    font-size: 26px;
    line-height: 38px;
  }
  .contact-list {
    list-style: none;
    margin: 22px 0 0;
    padding: 0;
  }
  .contact-list li {
    display: flex;
    font-size: 26px;
    line-height: 41.5px;
  }
  .contact-key {
    width: 47px;
    font-weight: 700;
  }
  .address {
    margin: 22px 0 0;
    font-style: normal;
    font-size: 26px;
    line-height: 42px;
  }
  .website {
    margin: 4px 0 0;
    font-size: 26px;
    line-height: 42px;
  }
  .brand-lockup {
    position: absolute;
    left: 492px;
    top: 1020px;
    display: flex;
    align-items: center;
    gap: 22px;
  }
  .brand-square {
    width: 62px;
    height: 62px;
    background: var(--brand-red);
  }
  .brand-name {
    font-weight: 800;
    font-size: 80px;
    line-height: 1;
    color: var(--ink);
    letter-spacing: -1px;
  }
</style>
</head>
<body>
  <div class="card">
    <header class="hero-band">
      <span class="hero-name">LedgaVue</span>
    </header>

    <section class="details">
      <h1 class="employee-name">Name Of Employee</h1>
      <p class="job-title">Job Title</p>

      <ul class="contact-list">
        <li><span class="contact-key">t</span><span>Telephone No.</span></li>
        <li><span class="contact-key">f</span><span>Fax No.</span></li>
        <li><span class="contact-key">m</span><span>Mobile No.</span></li>
        <li><span class="contact-key">e</span><span>Email Address</span></li>
      </ul>

      <address class="address">
        Office<br>
        Address Line 1<br>
        Address Line 2<br>
        City &amp; Postcode
      </address>
      <p class="website">Website</p>
    </section>

    <div class="brand-lockup">
      <span class="brand-square"></span>
      <span class="brand-name">LedgaVue</span>
    </div>
  </div>
</body>
</html>
```